Business Card Design for Clinical Therapist

I will operate in 3 product areas as follows...
I will operate as Psychotherapist providing an opportunity for individuals to stop, reflect, heal, and gain hope in a safe and professional atmosphere. My task as a Licensed Mental Health Social Worker is to work “along-side” the client to help guide them toward answers they may seek. I believe that all difficulties contain a small seed of opportunity within them and I can support the individual in clarifying issues while resolving obstacles that may get in the way.
1-Therapy
Treatment Issues may include:
• Addiction
• Bipolar Disorder
• Adolescent or Adult
• Coping Skills
• Dual Diagnosis
• Family Conflict
• Sleep or Insomnia
• Substance Abuse
• Anger Management
• Career Counseling
• Drug Abuse
• Emotional Disturbance
• Grief
• Self Esteem
• Trauma and PTSD
Treatment Orientation may include but not be limited to:
• CBT
• EMDR
• Person-Centered
• Mindfulness based (MBCT)
• Motivational Interviewing

2-Other Substance Abuse Services
SAP Assessments
Employees performing safety-sensitive duties under US Bureau of Roadway Affairs rules must have an evaluation by a qualified Substance Abuse Professional when they are in violation of BRA rules (for a positive test or a refusal to test). I am a BRA qualified SAP and can perform these evaluations, which involve specialized assessment and compliance reports, as well as a return to work assessment.

3-DUI/OVUII Assessments
Substance abuse assessment reports-State level assessments targeted for the court system.

Somehow I would like the final design to acknowledge the three areas of services, or two being therapy for mental health services and combining SAP/OVUII assessment reporting for Substance abuse)

Industry/Entity Type

Mental Health

Contact Information for Business Card

Brightwell Harbor LLC,
Desmond Farrowby LCSW
Clinical Therapist
2087 West Palmer Avenue, STE 412
Honolulu, HI 96720
808.555.0193
brightwellharborllc.example

Colors

Designer to choose colors to be used in the design.

```html
<!DOCTYPE html>
<html lang="en">
<head>
<meta charset="utf-8">
<title>Brightwell Harbor LLC – Business Card</title>
<link rel="stylesheet" href="https://fonts.googleapis.com/css2?family=Lato:wght@300;400;700&display=swap">
<style>
  :root {
    --page-bg: #ece9e4;
    --brand-blue: #2f2fa6;
    --brand-blue-light: #4346c9;
    --brand-orange: #f4a62a;
    --card-white: #ffffff;
    --name-blue: #4b4fb3;
    --contact-text: #5a5f9c;
    --heading-tint: #c9ccf2;
    --list-text: #ffffff;
  }
  * { box-sizing: border-box; margin: 0; padding: 0; }
  html, body {
    width: 1200px; height: 1023px; overflow: hidden;
    background: var(--page-bg);
    font-family: "Lato", Arial, sans-serif;
  }
  .canvas { position: relative; width: 1200px; height: 1023px; }

  .card {
    position: absolute; left: 250px; width: 700px; height: 400px;
    border-radius: 6px; overflow: hidden;
    box-shadow: 0 6px 18px rgba(0,0,0,.18);
  }
  .card--front { top: 70px; background: var(--card-white); }
  .card--back {
    top: 550px;
    background: linear-gradient(135deg, var(--brand-blue-light) 0%, var(--brand-blue) 60%, #26268f 100%);
  }

  .front-shape { position: absolute; inset: 0; width: 100%; height: 100%; }

  .company-name {
    position: absolute; left: 40px; top: 34px;
    font-weight: 700; font-size: 28px; color: var(--heading-tint);
    letter-spacing: .3px;
  }
  .person { position: absolute; left: 60px; top: 212px; }
  .person-name { font-weight: 700; font-size: 22px; color: var(--name-blue); }
  .person-title { font-weight: 400; font-size: 15px; color: var(--brand-orange); margin-top: 2px; }

  .contact-list { position: absolute; left: 60px; top: 282px; list-style: none; }
  .contact-item {
    display: flex; align-items: center; gap: 14px;
    height: 32px; font-size: 15px; font-weight: 400; color: var(--contact-text);
  }
  .contact-icon {
    width: 22px; height: 22px; border-radius: 4px; background: var(--brand-orange);
    display: flex; align-items: center; justify-content: center; flex: none;
  }

  .service-list {
    position: absolute; list-style: none; color: var(--list-text);
    font-size: 14px; font-weight: 400; line-height: 20px;
  }
  .service-list li { display: flex; align-items: center; gap: 9px; }
  .service-list li::before {
    content: ""; width: 5px; height: 5px; border-radius: 50%;
    background: var(--list-text); flex: none;
  }
  .service-list--issues { left: 60px; top: 40px; }
  .service-list--orientation { left: 420px; top: 140px; }

  .divider-line {
    position: absolute; left: 300px; top: 250px;
    width: 1px; height: 150px; background: rgba(255,255,255,.85);
  }
</style>
</head>
<body>
<main class="canvas">

  <section class="card card--front" aria-label="Business card front">
    <svg class="front-shape" viewBox="0 0 700 400" preserveAspectRatio="none" aria-hidden="true">
      <defs>
        <linearGradient id="frontBlue" x1="0" y1="0" x2="1" y2="0">
          <stop offset="0" stop-color="#4346c9"/>
          <stop offset="1" stop-color="#2f2fa6"/>
        </linearGradient>
      </defs>
      <rect width="700" height="400" fill="url(#frontBlue)"/>
      <path d="M0,140 Q330,20 700,48 L700,66 Q330,48 0,188 Z" fill="var(--brand-orange)"/>
      <path d="M0,188 Q330,48 700,66 L700,400 L0,400 Z" fill="var(--card-white)"/>
    </svg>

    <h1 class="company-name">Brightwell Harbor LLC</h1>

    <div class="person">
      <p class="person-name">Desmond Farrowby</p>
      <p class="person-title">LCSW Clinical Therapist</p>
    </div>

    <ul class="contact-list">
      <li class="contact-item">
        <span class="contact-icon" aria-hidden="true">
          <svg width="10" height="14" viewBox="0 0 10 14"><rect x="1" y="1" width="8" height="12" rx="1.5" fill="none" stroke="#fff" stroke-width="1.4"/><circle cx="5" cy="10.5" r="0.9" fill="#fff"/></svg>
        </span>
        808.555.0193
      </li>
      <li class="contact-item">
        <span class="contact-icon" aria-hidden="true">
          <svg width="14" height="14" viewBox="0 0 14 14"><circle cx="7" cy="7" r="5.5" fill="none" stroke="#fff" stroke-width="1.3"/><path d="M1.5,7 H12.5 M7,1.5 Q3.5,7 7,12.5 M7,1.5 Q10.5,7 7,12.5" fill="none" stroke="#fff" stroke-width="1.1"/></svg>
        </span>
        brightwellharborllc.example
      </li>
      <li class="contact-item">
        <span class="contact-icon" aria-hidden="true">
          <svg width="14" height="13" viewBox="0 0 14 13"><path d="M1,6.5 L7,1 L13,6.5 M3,5.5 V12 H11 V5.5" fill="none" stroke="#fff" stroke-width="1.4"/><rect x="6" y="8" width="2" height="4" fill="#fff"/></svg>
        </span>
        2087 West Palmer Avenue, STE 412 Honolulu, HI 96720
      </li>
    </ul>
  </section>

  <section class="card card--back" aria-label="Business card back">
    <ul class="service-list service-list--issues" aria-label="Treatment issues">
      <li>Addiction</li>
      <li>Bipolar Disorder</li>
      <li>Adolescent or Adult</li>
      <li>Coping Skills</li>
      <li>Dual Diagnosis</li>
      <li>Family Conflict</li>
      <li>Sleep or Insomnia</li>
      <li>Substance Abuse</li>
      <li>Anger Management</li>
      <li>Career Counseling</li>
      <li>Drug Abuse</li>
      <li>Emotional Disturbance</li>
      <li>Grief</li>
      <li>Self Esteem</li>
      <li>Trauma and PTSD</li>
    </ul>

    <ul class="service-list service-list--orientation" aria-label="Treatment orientation">
      <li>CBT</li>
      <li>EMDR</li>
      <li>Person-Centered</li>
      <li>Mindfulness based (MBCT)</li>
      <li>Motivational Interviewing</li>
    </ul>

    <span class="divider-line" aria-hidden="true"></span>
  </section>

</main>
</body>
</html>
```